Veltrix web stylesheet and logo

We are developing a new site for Veltrix and would like someone to provide a new logo and a web page style guide.
This company connects carriers with with customers that need specialty moves: store fixtures, displays, exhibits, technology, manufacturing equipment, etc.
We want to convey quality customer service, quality transportation, and the use of current technology in our business. We do not want to look like a trucking company.
Logo needs a total remake!!!

Target Market(s)

Technology, Retail, Manufacturing, Hospitalty...

Industry/Entity Type

It Company

Logo Text

we will provide some thing soon

Number of Pages Required

1 page

Font styles to use
Serif
Sans Serif

Requirements
Must have
• Warm colors, professional looking.
Nice to have
• If you have pics to include we'll consider
Should not have
• We must no look like a trucking company.

```html
<!DOCTYPE html>
<html lang="en">
<head>
<meta charset="utf-8">
<title>Veltrix — Specialty Moves</title>
<link href="https://fonts.googleapis.com/css2?family=Open+Sans:ital,wght@0,400;0,600;0,700;0,800;1,700;1,800&display=swap" rel="stylesheet">
<style>
:root{
  --red:#a00b0b;
  --red-dark:#7d0606;
  --ink:#1d1d1d;
  --dark:#1b1b1b;
  --text:#3c3c3c;
  --page:#e8e8e8;
  --soft:#f1f1f1;
  --white:#ffffff;
}
*{margin:0;padding:0;box-sizing:border-box}
html,body{width:1200px;height:2889px;overflow:hidden}
body{background:var(--page);font-family:"Open Sans",Arial,sans-serif;color:var(--text);position:relative}
.abs{position:absolute}
.sheet{position:absolute;left:15px;width:1170px}

/* header */
.header{top:0;height:135px;background:var(--white);border-bottom:4px solid var(--red)}
.contact-pill{left:657px;top:15px;width:484px;height:36px;background:var(--red);border-radius:0 0 0 6px;display:flex;align-items:center;gap:26px;padding-left:40px;color:#fff;font-size:14px;font-weight:700}
.contact-pill span{display:flex;align-items:center;gap:8px}
.socials{display:flex;gap:5px;margin-left:22px}
.socials i{width:20px;height:20px;border:2px solid #fff;border-radius:50%;display:block}
.brand{left:35px;top:58px;display:flex;align-items:center;gap:10px;font-size:36px;font-weight:800;color:var(--ink);letter-spacing:1px}
.brand b{width:28px;height:28px;border-radius:50%;background:var(--red);display:block}
.nav{right:30px;top:84px;display:flex;gap:32px;font-size:15px;font-weight:700;color:var(--ink);text-transform:uppercase}
.nav a{display:flex;align-items:center;gap:7px;color:inherit;text-decoration:none}
.nav a.active{color:var(--red)}

/* hero */
.hero{top:135px;height:718px;background:linear-gradient(160deg,#3b3d45 0%,#8a5a3a 25%,#5b2a22 45%,#2e2020 70%,#1c1c1c 100%)}
.hero-title{left:73px;top:212px;color:#fff;font-size:32px;line-height:44px;font-weight:800;font-style:italic;text-transform:uppercase}
.estimate{left:780px;top:48px;width:316px;height:379px;border:2px solid #fff;border-radius:4px;background:rgba(0,0,0,.6)}
.estimate-tab{left:770px;top:73px;width:336px;height:42px;background:var(--red);color:#fff;font-weight:700;font-size:18px;text-transform:uppercase;display:flex;align-items:center;justify-content:center}
.field{left:797px;width:280px;height:34px;display:flex;gap:7px}
.field .ico{width:30px;background:#f3f3f3;border-radius:3px;display:flex;align-items:center;justify-content:center}
.field .box{flex:1;background:#f3f3f3;border-radius:3px;font-size:12px;font-weight:600;color:#333;padding:9px 10px;text-transform:uppercase;position:relative}
.submit{left:780px;top:384px;width:316px;text-align:center;color:#fff;font-size:13px;font-weight:700}
.features{left:0;top:549px;width:1170px;height:169px;background:linear-gradient(#2a2626,#161616)}
.feature{top:515px;width:200px;text-align:center;color:#fff;font-size:15px;font-weight:700;text-transform:uppercase;line-height:19px}
.feature .badge{width:96px;height:96px;margin:0 auto 14px;border-radius:50%;background:var(--red);display:flex;align-items:center;justify-content:center}
.feature .badge i{width:70px;height:70px;border-radius:50%;background:#1c1c1c;border:3px solid #fff;display:flex;align-items:center;justify-content:center}

/* section headings */
.heading{left:0;width:1170px;display:flex;align-items:center;justify-content:center;gap:14px;font-size:28px;font-weight:800;text-transform:uppercase;color:var(--ink)}
.heading::before,.heading::after{content:"";width:110px;height:1px;background:#bbb}
.heading .dot{width:30px;height:30px;border-radius:50%;background:var(--red)}
.heading em{color:var(--red);font-style:italic}
.heading.light{color:#fff}
.heading.light em{color:#fff}
.btn{height:38px;border-radius:5px;display:flex;align-items:center;justify-content:center;gap:14px;font-size:14px;font-weight:700;text-transform:uppercase}
.btn .dot{width:22px;height:22px;border-radius:50%;background:var(--red)}

/* about */
.about{top:853px;height:403px;background:var(--white)}
.about p{position:absolute;left:95px;width:980px;text-align:center;font-size:13px;line-height:20px;color:#444}

/* services */
.services{top:1256px;height:483px;background:linear-gradient(180deg,#3b4453 0%,#22262e 50%,#4a4f58 100%)}
.services .sub{left:0;width:1170px;top:130px;text-align:center;color:#fff;font-size:17px;font-weight:700}
.service{top:178px;width:200px;text-align:center;color:#fff;font-size:15px;font-weight:700;text-transform:uppercase;line-height:20px}
.service .ring{width:118px;height:118px;margin:0 auto 22px;border-radius:50%;background:#e6e6e6;display:flex;align-items:center;justify-content:center}
.service .ring i{width:94px;height:94px;border-radius:50%;background:#1e1e1e;display:flex;align-items:center;justify-content:center}

/* news */
.news{top:1739px;height:403px;background:var(--white)}
.card{top:149px;width:324px;height:198px}
.card .photo{position:absolute;left:0;top:0;width:324px;height:158px}
.card .bar{position:absolute;left:0;top:158px;width:324px;height:40px;background:#e3e3e3;display:flex;justify-content:space-between;align-items:center;font-size:15px;font-weight:700;color:#222}
.card .bar span{padding-left:18px}
.card .bar a{height:40px;background:#2b2b2b;color:#fff;font-size:13px;font-weight:600;display:flex;align-items:center;gap:8px;padding:0 14px;text-decoration:none}
.date{top:-22px;left:-22px;width:100px;height:100px;border-radius:50%;background:var(--red);border:4px solid #fff;box-shadow:0 0 0 2px var(--red);color:#fff;text-align:center;font-weight:700;padding-top:10px;line-height:1.15}
.date .m{font-size:15px}
.date .d{font-size:25px}
.date .y{font-size:14px}

/* testimonials */
.testimonials{top:2142px;height:404px;background:var(--soft)}
.quote{left:239px;top:131px;width:694px;height:140px;background:#fff;border:1px solid #d8d8d8;border-radius:8px;padding:18px 28px 0 58px;font-size:14px;line-height:20px;color:#333}
.quote::after{content:"";position:absolute;left:30px;bottom:-12px;width:22px;height:22px;background:#fff;border-right:1px solid #d8d8d8;border-bottom:1px solid #d8d8d8;transform:rotate(45deg)}
.qm{font-size:44px;font-weight:800;color:#333;line-height:1;font-family:Georgia,serif}
.author{left:242px;top:290px;font-size:17px;font-weight:700;font-style:italic;color:#222}
.dots{left:0;width:1170px;top:337px;display:flex;justify-content:center;gap:5px}
.dots i{width:12px;height:12px;border-radius:50%;border:1px solid #777;display:block}
.dots i.on{background:var(--red);border-color:var(--red)}

/* footer */
.footer{top:2546px;height:295px;background:var(--dark);color:#fff}
.footer h4{position:absolute;top:45px;font-size:14px;font-weight:700;color:var(--red);text-transform:uppercase;padding-bottom:8px;border-bottom:1px solid #555}
.links{left:413px;top:82px;font-size:13px;font-weight:600;line-height:19.5px;list-style:none}
.office{left:588px;top:82px;font-size:13px;font-weight:600;line-height:25px}
.office .row{display:flex;gap:10px;align-items:flex-start}
.mini{left:852px;width:222px;height:30px;background:#000;font-size:11px;font-weight:700;padding:7px 8px}
.mini-submit{left:852px;top:216px;width:96px;height:28px;background:#5a5a5a;font-size:12px;font-weight:700;display:flex;align-items:center;justify-content:center}
.foot-brand{left:95px;top:132px;display:flex;align-items:center;gap:10px;font-size:32px;font-weight:800;letter-spacing:1px;color:#fff}
.foot-brand b{width:24px;height:24px;border-radius:50%;background:var(--red);display:block}
.legal{top:2841px;height:33px;background:var(--red);color:#fff;font-size:11px;font-weight:600;display:flex;align-items:center;justify-content:space-between;padding:0 22px}
.legal .socials i{width:18px;height:18px}
</style>
</head>
<body>

<!-- Header -->
<header class="sheet header">
  <div class="abs contact-pill">
    <span><svg width="16" height="16" viewBox="0 0 24 24"><circle cx="12" cy="12" r="11" fill="none" stroke="#fff" stroke-width="2"/><path d="M8 6l2 3-1 1.5c.8 1.8 2 3 3.6 3.7L14 13l3 2-1 2.5C11 17 7 13 6.5 8z" fill="#fff"/></svg>1.800.555.0142</span>
    <span><svg width="16" height="16" viewBox="0 0 24 24"><circle cx="12" cy="12" r="11" fill="none" stroke="#fff" stroke-width="2"/><rect x="6" y="8" width="12" height="8" fill="none" stroke="#fff" stroke-width="1.6"/><path d="M6 8l6 4 6-4" fill="none" stroke="#fff" stroke-width="1.6"/></svg>info@veltrix.com</span>
    <div class="socials"><i></i><i></i><i></i></div>
  </div>
  <div class="abs brand"><b></b>VELTRIX</div>
  <nav class="abs nav">
    <a class="active" href="#"><svg width="16" height="14" viewBox="0 0 16 14"><path d="M8 0L0 7h2v7h4V9h4v5h4V7h2z" fill="currentColor"/></svg>Home</a>
    <a href="#"><svg width="16" height="16" viewBox="0 0 16 16"><circle cx="8" cy="8" r="6" fill="none" stroke="currentColor" stroke-width="3"/></svg>About</a>
    <a href="#"><svg width="16" height="16" viewBox="0 0 16 16"><circle cx="8" cy="8" r="5" fill="none" stroke="currentColor" stroke-width="2.5" stroke-dasharray="3 2"/></svg>Services</a>
    <a href="#"><svg width="16" height="14" viewBox="0 0 16 14"><path d="M1 1h14v9H6l-4 3v-3H1z" fill="none" stroke="currentColor" stroke-width="1.6"/></svg>Testimonials</a>
    <a href="#"><svg width="16" height="14" viewBox="0 0 16 14"><rect x="1" y="1" width="14" height="12" fill="none" stroke="currentColor" stroke-width="1.6"/><path d="M4 5h8M4 8h8" stroke="currentColor" stroke-width="1.4"/></svg>News</a>
    <a href="#"><svg width="12" height="16" viewBox="0 0 12 16"><path d="M6 1v8M3 6v5c0 2 1.5 4 3 4s4-1 4-4V7" fill="none" stroke="currentColor" stroke-width="2"/></svg>Contact</a>
  </nav>
</header>

<!-- Hero -->
<section class="sheet hero" role="img" aria-label="Photo of a red semi-trailer on an open road at sunset">
  <h1 class="abs hero-title">We connect carriers<br>with customers for<br>specialty moves</h1>

  <div class="abs estimate"></div>
  <div class="abs estimate-tab">Request a free estimate</div>
  <div class="abs field" style="top:142px"><div class="ico"><svg width="14" height="14" viewBox="0 0 14 14"><circle cx="7" cy="4" r="3" fill="#333"/><path d="M1 14c0-4 3-6 6-6s6 2 6 6z" fill="#333"/></svg></div><div class="box">Name</div></div>
  <div class="abs field" style="top:184px"><div class="ico"><svg width="14" height="14" viewBox="0 0 24 24"><path d="M6 2l4 5-2 2c1.5 3 4 5.5 7 7l2-2 5 4-2 4C10 21 3 14 2 4z" fill="#333"/></svg></div><div class="box">Phone</div></div>
  <div class="abs field" style="top:226px"><div class="ico" style="font-weight:700;color:#333">@</div><div class="box">Email</div></div>
  <div class="abs field" style="top:268px"><div class="ico"><svg width="14" height="14" viewBox="0 0 14 14"><circle cx="7" cy="7" r="5.5" fill="none" stroke="#333" stroke-width="2"/><circle cx="7" cy="7" r="2" fill="#333"/></svg></div><div class="box">Service needed<svg style="position:absolute;right:0;top:0" width="30" height="34" viewBox="0 0 30 34"><path d="M0 0v34" stroke="#ccc"/><path d="M10 14h10l-5 6z" fill="#333"/></svg></div></div>
  <div class="abs field" style="top:310px;height:64px"><div class="ico" style="align-items:flex-start;padding-top:10px"><svg width="14" height="12" viewBox="0 0 14 12"><rect x="0" y="1" width="14" height="10" fill="#333"/><path d="M0 1l7 5 7-5" fill="none" stroke="#f3f3f3" stroke-width="1.4"/></svg></div><div class="box">Message</div></div>
  <div class="abs submit">SUBMIT</div>

  <div class="abs features"></div>
  <div class="abs feature" style="left:93px"><div class="badge"><i><svg width="34" height="34" viewBox="0 0 34 34"><rect x="3" y="5" width="26" height="26" rx="4" fill="none" stroke="#fff" stroke-width="3"/><path d="M9 17l6 6 15-16" fill="none" stroke="#fff" stroke-width="4"/></svg></i></div>Industry<br>Leader</div>
  <div class="abs feature" style="left:341px"><div class="badge"><i><svg width="36" height="30" viewBox="0 0 36 30"><path d="M18 2l4.5 9 10 1.5-7.3 7 1.8 10L18 24.8 9 29.5l1.8-10-7.3-7 10-1.5z" fill="#fff"/></svg></i></div>Quality customer<br>service</div>
  <div class="abs feature" style="left:592px"><div class="badge"><i><svg width="40" height="30" viewBox="0 0 40 30"><rect x="2" y="4" width="22" height="16" fill="none" stroke="#fff" stroke-width="2.5"/><path d="M24 9h8l5 6v5H24z" fill="none" stroke="#fff" stroke-width="2.5"/><circle cx="10" cy="23" r="3.5" fill="#fff"/><circle cx="30" cy="23" r="3.5" fill="#fff"/><path d="M8 10h10M8 14h8" stroke="#fff" stroke-width="2"/></svg></i></div>Quality<br>transportation</div>
  <div class="abs feature" style="left:840px"><div class="badge"><i><svg width="28" height="36" viewBox="0 0 28 36"><path d="M14 2C7 2 2 7 2 14c0 9 12 20 12 20s12-11 12-20C26 7 21 2 14 2z" fill="none" stroke="#fff" stroke-width="3"/><circle cx="14" cy="14" r="4.5" fill="#fff"/></svg></i></div>Advanced<br>technology</div>
</section>

<!-- About -->
<section class="sheet about">
  <h2 class="abs heading" style="top:54px"><span class="dot"></span>About <em>Veltrix</em></h2>
  <p style="top:128px">Lorem ipsum dolor sit amet, consectetuer adipiscing elit, sed diam nonummy nibh euismod tincidunt ut laoreet dolore magna aliquam erat volutpat. Ut wisi enim ad minim veniam, quis nostrud exerci tation ullamcorper suscipit lobortis nisl ut aliquip ex ea commodo consequat. Duis autem vel eum iriure dolor in hendrerit in vulputate velit esse molestie consequat, vel illum dolore eu feugiat nulla facilisis at vero eros et accumsan et iusto odio dignissim qui blandit praesent.</p>
  <p style="top:210px">Nam liber tempor cum soluta nobis eleifend option congue nihil imperdiet doming id quod mazim placerat facer possim assum. Typi non habent claritatem insitam usus legentis in iis qui facit eorum claritatem. Investigationes demonstraverunt lectores legere me lius quod ii legunt saepius. Claritas est etiam processus dynamicus, qui sequitur mutationem consuetudium lectorum.</p>
  <a class="abs btn" href="#" style="left:470px;top:308px;width:230px;background:#222;color:#fff;text-decoration:none"><span class="dot"></span>More about us</a>
</section>

<!-- Services -->
<section class="sheet services" role="img" aria-label="Photo of a city skyline with a cargo plane overhead and motion-blurred road">
  <h2 class="abs heading light" style="top:55px"><span class="dot"></span>Our <em>Services</em></h2>
  <div class="abs sub">We connect carriers with customers that need specialty moves for</div>
  <div class="abs service" style="left:78px"><div class="ring"><i><svg width="52" height="52" viewBox="0 0 52 52"><rect x="8" y="40" width="22" height="6" fill="#fff"/><path d="M19 40V28l12-12 10 6" fill="none" stroke="#fff" stroke-width="5"/><circle cx="31" cy="16" r="4" fill="#fff"/><path d="M40 22l4-2m-4 2l2 5" stroke="#fff" stroke-width="3"/></svg></i></div>Manufacturing<br>equipment</div>
  <div class="abs service" style="left:290px"><div class="ring"><i><svg width="52" height="52" viewBox="0 0 52 52"><path d="M6 12h40l-3 10H9z" fill="#fff"/><rect x="10" y="24" width="32" height="20" fill="none" stroke="#fff" stroke-width="3"/><rect x="16" y="30" width="8" height="14" fill="#fff"/><rect x="28" y="30" width="9" height="7" fill="none" stroke="#fff" stroke-width="2"/></svg></i></div>Store fixtures</div>
  <div class="abs service" style="left:500px"><div class="ring"><i><svg width="52" height="52" viewBox="0 0 52 52"><rect x="6" y="10" width="32" height="22" rx="2" fill="none" stroke="#fff" stroke-width="3"/><path d="M16 38h12" stroke="#fff" stroke-width="3"/><rect x="30" y="22" width="16" height="22" rx="2" fill="#1e1e1e" stroke="#fff" stroke-width="3"/></svg></i></div>Technology</div>
  <div class="abs service" style="left:710px"><div class="ring"><i><svg width="52" height="52" viewBox="0 0 52 52"><rect x="6" y="10" width="40" height="26" fill="none" stroke="#fff" stroke-width="3"/><path d="M6 18h40" stroke="#fff" stroke-width="2"/><rect x="12" y="22" width="8" height="9" fill="#fff"/><rect x="24" y="22" width="8" height="9" fill="#fff"/><rect x="36" y="22" width="5" height="9" fill="#fff"/><path d="M12 36v8M40 36v8" stroke="#fff" stroke-width="3"/></svg></i></div>Displays</div>
  <div class="abs service" style="left:920px"><div class="ring"><i><svg width="52" height="52" viewBox="0 0 52 52"><rect x="20" y="6" width="12" height="12" fill="#fff"/><rect x="14" y="20" width="24" height="8" fill="#fff"/><rect x="10" y="30" width="32" height="16" fill="none" stroke="#fff" stroke-width="3"/><path d="M18 30v16M26 30v16M34 30v16" stroke="#fff" stroke-width="2"/></svg></i></div>Exhibits</div>
  <a class="abs btn" href="#" style="left:470px;top:393px;width:230px;background:#fff;color:#222;text-decoration:none"><span class="dot"></span>More on services</a>
</section>

<!-- News -->
<section class="sheet news">
  <h2 class="abs heading" style="top:57px"><span class="dot"></span>Latest <em>News</em></h2>
  <article class="abs card" style="left:77px">
    <div class="photo" role="img" aria-label="Photo of a highway leading into a city at dusk" style="background:linear-gradient(160deg,#8c9bb0,#3f4c60 60%,#1f2633)"></div>
    <div class="bar"><span>News Title #1</span><a href="#">READ MORE <svg width="7" height="11" viewBox="0 0 7 11"><path d="M1 1l4.5 4.5L1 10" fill="none" stroke="#fff" stroke-width="1.8"/></svg></a></div>
    <div class="abs date"><div class="m">OCT</div><div class="d">16</div><div class="y">2016</div></div>
  </article>
  <article class="abs card" style="left:432px">
    <div class="photo" role="img" aria-label="Photo of a red truck trailer at sunset" style="background:linear-gradient(160deg,#e8a35c,#7a3a2a 45%,#2f2a2a)"></div>
    <div class="bar"><span>News Title #2</span><a href="#">READ MORE <svg width="7" height="11" viewBox="0 0 7 11"><path d="M1 1l4.5 4.5L1 10" fill="none" stroke="#fff" stroke-width="1.8"/></svg></a></div>
    <div class="abs date"><div class="m">OCT</div><div class="d">08</div><div class="y">2016</div></div>
  </article>
  <article class="abs card" style="left:788px">
    <div class="photo" role="img" aria-label="Photo of a hand using a tablet showing a chart" style="background:linear-gradient(160deg,#ffffff,#dfe3e8 55%,#9aa4b0)"></div>
    <div class="bar"><span>News Title #3</span><a href="#">READ MORE <svg width="7" height="11" viewBox="0 0 7 11"><path d="M1 1l4.5 4.5L1 10" fill="none" stroke="#fff" stroke-width="1.8"/></svg></a></div>
    <div class="abs date"><div class="m">OCT</div><div class="d">06</div><div class="y">2016</div></div>
  </article>
</section>

<!-- Testimonials -->
<section class="sheet testimonials">
  <h2 class="abs heading" style="top:53px"><span class="dot"></span>Words from <em>Happy Customers</em></h2>
  <blockquote class="abs quote">
    <span class="abs qm" style="left:18px;top:14px">&ldquo;</span>
    Lorem ipsum dolor sit amet, consectetuer adipiscing elit, sed diam nonummy nibh euismod tincidunt ut laoreet dolore magna aliquam erat volutpat. Ut wisi enim ad minim veniam, quis nostrud exerci tation ullamcorper suscipit lobortis nisl ut aliquip ex ea commodo consequat. Duis autem vel eum iriure dolor in hendrerit in vulputate velit esse molestie consequat, vel illum dolore eu feugiat nulla facilisis at vero. <span class="qm" style="font-size:30px;vertical-align:-12px">&rdquo;</span>
  </blockquote>
  <div class="abs author">Clara Dunmore</div>
  <div class="abs dots"><i class="on"></i><i></i><i></i><i></i></div>
</section>

<!-- Footer -->
<footer class="sheet footer">
  <div class="abs foot-brand"><b></b>VELTRIX</div>
  <h4 style="left:413px;width:160px">Quick Links</h4>
  <ul class="abs links">
    <li>· Home</li><li>· About</li><li>· Services</li><li>· Testimonials</li><li>· News</li><li>· Contact</li>
  </ul>
  <h4 style="left:588px;width:205px">Head Office</h4>
  <div class="abs office">
    <div class="row"><svg width="20" height="20" viewBox="0 0 20 20" style="margin-top:3px"><circle cx="10" cy="10" r="9" fill="none" stroke="#fff" stroke-width="1.5"/><path d="M10 4c-2.5 0-4 1.7-4 4 0 3 4 7 4 7s4-4 4-7c0-2.3-1.5-4-4-4z" fill="#fff"/></svg><div>VELTRIX<br>123 Lorem Ipsum Dr<br>Fairhaven, CA 90112</div></div>
    <div class="row" style="margin-top:20px"><svg width="20" height="20" viewBox="0 0 20 20" style="margin-top:3px"><circle cx="10" cy="10" r="9" fill="none" stroke="#fff" stroke-width="1.5"/><path d="M7 5l1.8 2.4-1 1.2c.7 1.6 1.8 2.7 3.2 3.3l1.2-1L14.5 13l-.9 2C9.5 14.7 6 11 5.7 6.7z" fill="#fff"/></svg><div>Toll Free: 1-800-555-0142</div></div>
    <div class="row" style="margin-top:20px"><svg width="20" height="20" viewBox="0 0 20 20" style="margin-top:3px"><circle cx="10" cy="10" r="9" fill="none" stroke="#fff" stroke-width="1.5"/><rect x="5" y="7" width="10" height="7" fill="none" stroke="#fff" stroke-width="1.3"/><path d="M5 7l5 3.5L15 7" fill="none" stroke="#fff" stroke-width="1.3"/></svg><div>info@veltrix.com</div></div>
  </div>
  <h4 style="left:852px;width:222px">Quick Message</h4>
  <div class="abs mini" style="top:88px">NAME</div>
  <div class="abs mini" style="top:122px">EMAIL</div>
  <div class="abs mini" style="top:156px;height:54px">MESSAGE</div>
  <div class="abs mini-submit">SUBMIT</div>
</footer>
<div class="sheet legal">
  <span>© 2016 VELTRIX. ALL RIGHTS RESERVED.</span>
  <div class="socials"><i></i><i></i><i></i></div>
</div>

</body>
</html>
```